Advertisement Sign

Hello,
We're in need of a new design for an advertisement sign. Below is our current concept, but we're looking for improvements. Specifically, we'd like to enhance the size of the 'Call for Assistance' text, possibly explore different fonts, and possibly add a background to make the design more engaging and less plain. We need something that sticks out more. Any suggestions are welcome.

Target Market(s)

Construction and Landscape Companies

```html
<!DOCTYPE html>
<html lang="en">
<head>
<meta charset="UTF-8">
<title>Ridgeway Rentals – Roadside Sign</title>
<link href="https://fonts.googleapis.com/css2?family=Montserrat:wght@600;700;800&display=swap" rel="stylesheet">
<style>
  :root {
    --ink: #232323;
    --band: #282828;
    --blue: #2b74bf;
    --grey: #707070;
    --paper: #ffffff;
    --page: #ffffff;
    --edge: #3a3a3a;
  }
  * { box-sizing: border-box; margin: 0; padding: 0; }
  html, body {
    width: 975px;
    height: 1200px;
    overflow: hidden;
    background: var(--page);
    font-family: "Montserrat", Arial, sans-serif;
  }
  .canvas {
    position: relative;
    width: 975px;
    height: 1200px;
  }
  .sign {
    position: absolute;
    left: 112px;
    top: 412px;
    width: 751px;
    height: 376px;
    border: 1px solid var(--edge);
    background: var(--paper);
    display: flex;
    flex-direction: column;
  }
  .sign__brand {
    height: 228px;
    display: flex;
    flex-direction: column;
    align-items: center;
    justify-content: center;
    gap: 22px;
  }
  .brand {
    display: flex;
    align-items: center;
    gap: 20px;
  }
  .brand__square {
    width: 58px;
    height: 58px;
    background: var(--blue);
  }
  .brand__name {
    font-weight: 800;
    font-size: 52px;
    line-height: 1;
    color: var(--ink);
    text-transform: uppercase;
    letter-spacing: 1px;
  }
  .tagline {
    display: flex;
    align-items: center;
    gap: 22px;
  }
  .tagline__rule {
    width: 84px;
    height: 3px;
    background: var(--grey);
  }
  .tagline__text {
    font-weight: 700;
    font-size: 14px;
    letter-spacing: 4px;
    color: var(--grey);
    text-transform: uppercase;
  }
  .sign__contact {
    flex: 1;
    background: var(--band);
    color: var(--paper);
    display: flex;
    flex-direction: column;
    align-items: center;
    justify-content: center;
    gap: 4px;
  }
  .contact__call {
    font-weight: 700;
    font-size: 38px;
    line-height: 1;
    letter-spacing: 0.5px;
    text-transform: uppercase;
  }
  .contact__phone {
    font-weight: 700;
    font-size: 76px;
    line-height: 1;
    letter-spacing: 6px;
  }
</style>
</head>
<body>
  <main class="canvas">
    <section class="sign">
      <div class="sign__brand">
        <div class="brand">
          <span class="brand__square"></span>
          <span class="brand__name">Ridgeway Rentals</span>
        </div>
        <div class="tagline">
          <span class="tagline__rule"></span>
          <span class="tagline__text">Built To Move Ahead</span>
          <span class="tagline__rule"></span>
        </div>
      </div>
      <div class="sign__contact">
        <p class="contact__call">Call For Assistance</p>
        <p class="contact__phone">403-555-0147</p>
      </div>
    </section>
  </main>
</body>
</html>
```